VORK Business Cards, Letterhead and Envelopes
Business Cards, Letterhead and Envelopes
Simple
Rajendran P Subbiah
Dirección TI - ERP Quandrel
Calle Tepozan 58,
Col. Las Brisas,
Distrito Federal
Mexico - 04260
rajen@vorkitel.mx
www.vorkitel.mx, www.vorkitel.in

```html
<!DOCTYPE html>
<html lang="en">
<head>
<meta charset="utf-8">
<title>VORK Stationery Set</title>
<link href="https://fonts.googleapis.com/css2?family=Arimo:wght@400;700&display=swap" rel="stylesheet">
<style>
  :root {
    --backdrop: #3d3d3d;
    --paper: #ffffff;
    --brand-blue: #2340b0;
    --ink: #333333;
    --fold-line: #d4d4d4;
  }
  * { margin: 0; padding: 0; box-sizing: border-box; }
  html, body { width: 1200px; height: 684px; overflow: hidden; }
  body {
    background: var(--backdrop);
    font-family: "Arimo", Arial, sans-serif;
    color: var(--ink);
    position: relative;
  }
  .sheet {
    position: absolute;
    background: var(--paper);
    box-shadow: 0 2px 6px rgba(0,0,0,0.45);
    overflow: hidden;
  }
  .band { position: absolute; left: 0; right: 0; background: var(--brand-blue); }
  .brand {
    position: absolute;
    display: flex; align-items: center; gap: 5px;
    color: var(--brand-blue);
    font-weight: 700;
    letter-spacing: 0.5px;
    white-space: nowrap;
  }
  .brand-mark { background: var(--brand-blue); display: inline-block; }
  .centered { left: 50%; transform: translateX(-50%); }
  .fine-print {
    position: absolute; left: 0; right: 0;
    text-align: center;
    font-size: 4.5px; line-height: 7px;
    white-space: nowrap;
  }

  /* Letterhead */
  .letterhead { left: 192px; top: 60px; width: 437px; height: 595px; }
  .letterhead .band-top { top: 0; height: 7px; }
  .letterhead .band-bottom { bottom: 0; height: 17px; }
  .letterhead .brand { top: 30px; font-size: 30px; }
  .letterhead .brand-mark { width: 18px; height: 18px; }
  .letterhead .fine-print { bottom: 24px; }

  /* Business cards */
  .card { left: 48px; width: 132px; height: 108px; }
  .card-front { top: 240px; }
  .card-front .brand { top: 22px; font-size: 20px; }
  .card-front .brand-mark { width: 12px; height: 12px; }
  .card-front .tagline { position: absolute; left: 0; right: 0; top: 82px; text-align: center; font-size: 4.5px; }
  .card-front .band-bottom { bottom: 0; height: 4px; }

  .card-back { top: 365px; }
  .card-back .band-top { top: 0; height: 5px; }
  .card-back .band-bottom { bottom: 0; height: 6px; }
  .card-back .brand { left: 12px; top: 12px; font-size: 16px; }
  .card-back .brand-mark { width: 10px; height: 10px; }
  .contact { position: absolute; left: 12px; top: 52px; font-size: 4.4px; line-height: 6.3px; white-space: nowrap; }
  .contact .person { font-weight: 700; }

  /* Envelope back */
  .envelope-back { left: 641px; top: 106px; width: 504px; height: 232px; }
  .envelope-back svg { position: absolute; left: 0; top: 0; }
  .envelope-back .brand { top: 48px; font-size: 26px; }
  .envelope-back .brand-mark { width: 15px; height: 15px; }

  /* Envelope front */
  .envelope-front { left: 641px; top: 365px; width: 504px; height: 293px; }
  .envelope-front .band-top { top: 0; height: 12px; }
  .envelope-front .band-bottom { bottom: 0; height: 18px; }
  .envelope-front .brand { top: 36px; font-size: 26px; }
  .envelope-front .brand-mark { width: 15px; height: 15px; }
  .envelope-front .fine-print { bottom: 58px; }
</style>
</head>
<body>

  <section class="sheet letterhead" aria-label="Letterhead">
    <div class="band band-top"></div>
    <div class="brand centered"><span class="brand-mark"></span>VORK</div>
    <p class="fine-print">Calle Tepozan 58, Col. Las Brisas, Distrito Federal, Mexico - 04260 &nbsp;|&nbsp; T: +52 55 0000 0000 &nbsp;|&nbsp; rajen@vorkitel.mx<br>www.vorkitel.mx, www.vorkitel.in</p>
    <div class="band band-bottom"></div>
  </section>

  <section class="sheet card card-front" aria-label="Business card front">
    <div class="brand centered"><span class="brand-mark"></span>VORK</div>
    <p class="tagline">Welcome to the Network</p>
    <div class="band band-bottom"></div>
  </section>

  <section class="sheet card card-back" aria-label="Business card back">
    <div class="band band-top"></div>
    <div class="brand"><span class="brand-mark"></span>VORK</div>
    <div class="contact">
      <p class="person">Rajendran P Subbiah</p>
      <p>Dirección TI - ERP Quandrel</p>
      <p>Calle Tepozan 58, Col. Las Brisas,</p>
      <p>Distrito Federal, Mexico - 04260</p>
      <p>T: +52 55 0000 0000 &nbsp; rajen@vorkitel.mx</p>
      <p>www.vorkitel.mx, www.vorkitel.in</p>
    </div>
    <div class="band band-bottom"></div>
  </section>

  <section class="sheet envelope-back" aria-label="Envelope back">
    <svg width="504" height="232" viewBox="0 0 504 232">
      <path d="M0,0 Q110,150 252,158 Q394,150 504,0" fill="#fbfbfb" stroke="var(--fold-line)" stroke-width="1.5"/>
    </svg>
    <div class="brand centered"><span class="brand-mark"></span>VORK</div>
  </section>

  <section class="sheet envelope-front" aria-label="Envelope front">
    <div class="band band-top"></div>
    <div class="brand centered"><span class="brand-mark"></span>VORK</div>
    <p class="fine-print">Calle Tepozan 58, Col. Las Brisas, Distrito Federal, Mexico - 04260 &nbsp;|&nbsp; T: +52 55 0000 0000 &nbsp;|&nbsp; rajen@vorkitel.mx<br>www.vorkitel.mx, www.vorkitel.in</p>
    <div class="band band-bottom"></div>
  </section>

</body>
</html>
```